" A empresa opera um ecossistema que conecta o transporte público a benefícios sociais, permitindo que usuários de cartões de transporte possam acessar serviços de saúde, descontos e recargas integradas por meio de um modelo digital de adesão e refiliação. "

```html
<!DOCTYPE html>
<html lang="pt-BR">
<head>
<meta charset="UTF-8">
<title>Abrangência Nacional — O Futuro da Operação</title>
<link href="https://fonts.googleapis.com/css2?family=Comfortaa:wght@700&family=Montserrat:wght@400;500;700;800&display=swap" rel="stylesheet">
<style>
  :root {
    --page-bg: #ffffff;
    --band-bg: #102838;
    --band-bg-deep: #0b1f2c;
    --teal: #4fb6bf;
    --teal-muted: #2e6a78;
    --white: #ffffff;
    --text-soft: #dfe8ee;
    --map-grey: #cfd2d4;
    --map-green: #3fd878;
  }
  html, body {
    margin: 0;
    padding: 0;
    width: 1200px;
    height: 1200px;
    overflow: hidden;
    background: var(--page-bg);
    font-family: "Montserrat", sans-serif;
  }
  .canvas {
    position: relative;
    width: 1200px;
    height: 1200px;
  }
  .coverage-band {
    position: absolute;
    left: 0;
    top: 264px;
    width: 1200px;
    height: 672px;
    background: linear-gradient(100deg, var(--band-bg) 0%, var(--band-bg-deep) 100%);
  }
  .headline {
    position: absolute;
    left: 72px;
    top: 316px;
    margin: 0;
    font-weight: 400;
  }
  .headline-top {
    display: block;
    font-family: "Montserrat", sans-serif;
    font-weight: 500;
    font-size: 62px;
    line-height: 1;
    color: var(--teal);
    letter-spacing: 1px;
  }
  .headline-main {
    display: block;
    margin-top: 8px;
    font-family: "Comfortaa", sans-serif;
    font-weight: 700;
    font-size: 86px;
    line-height: 1;
    color: var(--white);
  }
  .subtitle {
    position: absolute;
    left: 72px;
    top: 482px;
    margin: 0;
    font-size: 34px;
    font-weight: 400;
    color: var(--white);
  }
  .title-rule {
    position: absolute;
    left: 72px;
    top: 550px;
    width: 486px;
    height: 3px;
    background: var(--teal);
  }
  .phase {
    position: absolute;
  }
  .phase h2 {
    margin: 0 0 8px;
    font-size: 22px;
    font-weight: 800;
    color: var(--teal);
    letter-spacing: 0.5px;
    white-space: nowrap;
  }
  .phase ul {
    list-style: none;
    margin: 0;
    padding: 0;
  }
  .phase li {
    font-size: 17px;
    line-height: 31px;
    color: var(--text-soft);
    white-space: nowrap;
  }
  .phase li::before {
    content: "·";
    margin-right: 4px;
  }
  .phase-proof { left: 72px; top: 620px; }
  .phase-2025 { left: 72px; top: 700px; }
  .phase-2026 { left: 403px; top: 618px; }
  .footer-bar {
    position: absolute;
    left: 72px;
    top: 874px;
    width: 643px;
    height: 16px;
    background: var(--teal-muted);
  }
  .coverage-map {
    position: absolute;
    left: 580px;
    top: 300px;
    width: 600px;
    height: 620px;
  }
</style>
</head>
<body>
  <main class="canvas">
    <div class="coverage-band"></div>

    <h1 class="headline">
      <span class="headline-top">Abrangência</span>
      <span class="headline-main">Nacional</span>
    </h1>
    <p class="subtitle">O Futuro da Operação</p>
    <div class="title-rule"></div>

    <section class="phase phase-proof">
      <h2>PROVA DE CONCEITO</h2>
      <ul><li>Florianópolis</li></ul>
    </section>

    <section class="phase phase-2025">
      <h2>EXPANSÃO 2025</h2>
      <ul>
        <li>Vitória e Vila Velha</li>
        <li>Goiânia</li>
      </ul>
    </section>

    <section class="phase phase-2026">
      <h2>EXPANSÃO 2026 (Capitais)</h2>
      <ul>
        <li>Salvador</li>
        <li>Belo Horizonte</li>
        <li>Rio de Janeiro</li>
        <li>Fortaleza</li>
        <li>Curitiba</li>
        <li>Região metropolitana (SP)</li>
      </ul>
    </section>

    <div class="footer-bar"></div>

    <svg class="coverage-map" viewBox="0 0 600 620" role="img" aria-label="Mapa 3D do Brasil com os estados de atuação destacados em verde e os demais em cinza">
      <defs>
        <linearGradient id="mapFill" x1="0" y1="0" x2="1" y2="0.6">
          <stop offset="0" stop-color="var(--map-grey)"/>
          <stop offset="0.5" stop-color="var(--map-grey)"/>
          <stop offset="0.75" stop-color="var(--map-green)"/>
          <stop offset="1" stop-color="var(--map-green)"/>
        </linearGradient>
      </defs>
      <path d="M40 0 H560 Q600 0 600 40 V580 Q600 620 560 620 H205 Q165 620 165 580 V300 Q165 270 135 270 H40 Q0 270 0 230 V40 Q0 0 40 0 Z" fill="url(#mapFill)" opacity="0.9"/>
    </svg>
  </main>
</body>
</html>
```